velvet harbor

We are in need of a website for married spouses or wives that are looking for a one night stand or affair, trying to get out from their marriage routine. We want our website for married people only.

i have extended my deadline until the 29 of april. we are looking for at least 8 pages if possible, but we would only like to see the first page as an example for the next few pages. if we really like your design we weill hire you and thenĀ  we talk about the rest of the pages and the money. if you have any comments or questions, don't be afraid to ask.

• We want to be able to have a link open to a future website. it needs pop ups and ads. we would like it to say at the bottom of the page, bolded and highlighted that, " We are not responsible for any sexually transmitted diseases" and " We are not responsible for any marriage break-ups or any problems in consequence after the encounters." " It is the responsibility of the subscriber(member) to have enough information about the person before the encounter." We would like the website to be compatible to zentrobe. The subscribers must be able to web chat, upload photos, and upload videos but can decide who can see them or watch them.They can also have the choice to block certain members from their profile.

```html
<!DOCTYPE html>
<html lang="en">
<head>
<meta charset="utf-8">
<title>Velvet Harbor – Member Profile</title>
<link href="https://fonts.googleapis.com/css2?family=Cabin:wght@400;600;700&family=Arimo:wght@400;700&display=swap" rel="stylesheet">
<style>
:root{
  --brown:#9c5a36;
  --brown-dark:#7e4529;
  --brown-band:#a86e45;
  --nav-top:#bb8359;
  --nav-bottom:#8a5234;
  --peach:#f4c78e;
  --cream:#fae6cc;
  --menu:#fde2b5;
  --menu-active:#c08a5c;
  --ink:#333;
  --ink-soft:#555;
  --footer:#bcbdbf;
  --footer-ink:#6a6a6a;
  --navy:#1f3b63;
  --white:#fff;
}
*{box-sizing:border-box;margin:0;padding:0}
html,body{width:831px;height:1200px;overflow:hidden;background:var(--white)}
body{font-family:"Arimo",Arial,sans-serif;color:var(--ink)}
.stage{position:relative;width:850px;height:1228px;transform:scale(0.97765);transform-origin:0 0;overflow:hidden}
.abs{position:absolute}

.top-zone{left:0;top:0;width:850px;height:558px;background:linear-gradient(#fff 0%,#fdf0e0 20%,var(--peach) 100%);border-bottom:1px solid #a9a29a}
.mid-zone{left:0;top:558px;width:850px;height:386px;background:var(--cream)}

.brand{left:100px;top:14px;font-family:"Cabin",sans-serif;font-weight:700;font-size:29px;color:var(--brown-dark);letter-spacing:.3px}
.ad-slot{left:396px;top:10px;width:366px;height:42px;background:#fff;border:1px solid #cfcfcf;border-radius:4px;font-size:17px;color:#a5a5a5;display:flex;align-items:center;justify-content:center}

.main-nav{left:86px;top:62px;width:678px;height:31px;border-radius:6px 6px 0 0;background:linear-gradient(var(--nav-top),var(--nav-bottom));display:flex;align-items:center}
.main-nav a{font-family:"Cabin",sans-serif;font-weight:700;font-size:11.5px;color:#fff;text-decoration:none;letter-spacing:.4px;display:flex;align-items:center;height:100%;padding:0 0 0 0;border-right:1px solid rgba(255,255,255,.18)}
.main-nav a:last-child{border-right:0}
.main-nav a.open{color:#f6d3a6}
.chev{display:inline-block;width:10px;height:10px;border-radius:50%;background:#6e3e25;margin-left:6px;position:relative}
.chev:after{content:"";position:absolute;left:3px;top:2.5px;border-left:4px solid #fff;border-top:2.5px solid transparent;border-bottom:2.5px solid transparent}

.dropdown{left:181px;top:93px;width:147px;height:61px;background:var(--menu);font-family:"Cabin",sans-serif;font-weight:700;font-size:9px;letter-spacing:.4px;color:var(--brown-dark)}
.dropdown li{list-style:none;height:19px;line-height:19px;padding-left:22px}
.dropdown li.active{background:var(--menu-active);color:#fbe3c2}

.h-section{font-family:"Cabin",sans-serif;font-weight:600;font-size:18px;color:#3b2a20}
.h-section b{color:var(--brown);font-weight:700}

.photo{border:1px solid #d9c6b0;border-radius:3px}
.main-photo{left:100px;top:170px;width:165px;height:241px;background:linear-gradient(135deg,#3a2b26,#c9a290 55%,#7d7a86)}

.details{left:293px;top:169px;font-size:8px;border-collapse:collapse}
.details td{height:15.6px;padding:0}
.details td:first-child{width:74px;color:#444}
.details .name{font-weight:700}
.stars{color:#e1303f;font-size:11px;letter-spacing:-1px}
.stars i{color:#c8c8c8;font-style:normal}

.intro{left:104px;top:443px;width:340px;font-size:8.2px;line-height:12.5px}
.intro strong{display:block;margin-bottom:10px}

.action-btn{height:25px;background:#fff;border:1px solid #ccc;border-radius:3px;font-size:8px;display:flex;align-items:center;padding-left:8px;gap:10px;color:#333}
.ico{width:17px;height:17px;border-radius:50%;flex:none}

.friend{left:508px;width:260px;height:62px}
.friend .face{position:absolute;left:0;top:0;width:64px;height:62px;border:2px solid #fff;border-radius:3px;background:linear-gradient(160deg,#e6d3c1,#b08a70)}
.friend .info{position:absolute;left:76px;top:3px;font-size:8px;line-height:11px;width:180px}
.friend .info b{display:block;margin-bottom:8px}

.pill{height:25px;border-radius:4px;background:linear-gradient(#b07853,#844b2e);color:#fff;font-family:"Cabin",sans-serif;font-weight:700;font-size:10.5px;letter-spacing:.4px;display:flex;align-items:center;padding-left:12px}
.pill .chev{background:#fff;margin-left:10px;width:13px;height:13px}
.pill .chev:after{border-left-color:#844b2e;left:5px;top:4px}

.thumb{width:107px;height:108px;border:1px solid #e2cdb4;border-radius:5px}

.add-info{left:509px;top:632px;width:258px;font-size:8.2px;line-height:13.7px}
.add-info strong{display:block;margin-bottom:14px}
.add-info p{margin-bottom:14px}

.notice-line{left:0;top:941px;width:850px;height:6px;background:#bdbdbd}
.notice-band{left:0;top:947px;width:850px;height:97px;background:var(--brown-band)}
.notice-tab{left:272px;top:928px;width:298px;height:31px;background:linear-gradient(#f8f9fb,#d2d6dc);border-radius:2px;font-weight:700;font-size:15px;color:var(--navy);display:flex;align-items:center;justify-content:center}
.notice-text{left:89px;top:971px;width:690px;font-weight:700;font-size:14px;line-height:19.5px;color:#fff}

.footer{left:0;top:1044px;width:850px;height:184px;background:var(--footer)}
.f-col{top:1075px;width:100px}
.f-col h3{font-family:"Cabin",sans-serif;font-weight:600;font-size:18px;color:var(--footer-ink);margin-bottom:4px}
.f-col a{display:block;font-size:9.5px;color:#555;text-decoration:none;height:27px;line-height:18px;border-bottom:1px solid #aeafb1}
.social{left:625px;top:1085px;display:flex;gap:8px}
.social span{width:20px;height:20px;border-radius:2px;background:#9ea0a3;border:1px solid #d8d9db}
.f-brand{left:585px;top:1127px;font-family:"Cabin",sans-serif;font-weight:700;font-size:22px;color:#7c7e81}
.copyright{left:586px;top:1160px;font-size:10px;color:#444}
</style>
</head>
<body>
<div class="stage">
  <div class="abs top-zone"></div>
  <div class="abs mid-zone"></div>

  <header>
    <div class="abs brand">VelvetHarbor</div>
    <div class="abs ad-slot">&lt;&lt; Place advert here &gt;&gt;</div>
    <nav class="abs main-nav">
      <a href="#" style="width:96px;padding-left:26px">HOME<span class="chev"></span></a>
      <a href="#" class="open" style="width:147px;padding-left:19px">YOUR ACCOUNT<span class="chev"></span></a>
      <a href="#" style="width:78px;padding-left:18px">JOIN<span class="chev"></span></a>
      <a href="#" style="width:80px;padding-left:16px">BLOG<span class="chev"></span></a>
      <a href="#" style="width:111px;padding-left:19px">CONTACT<span class="chev"></span></a>
      <a href="#" style="width:166px;padding-left:15px">CREATE NEW ACCOUNT</a>
    </nav>
  </header>

  <h1 class="abs h-section" style="left:99px;top:128px"><b>USER</b> Profile</h1>
  <ul class="abs dropdown">
    <li class="active">EDIT YOUR PROFIT</li>
    <li>YOUR GIFTS</li>
    <li>MESSAGES</li>
  </ul>

  <div class="abs photo main-photo" role="img" aria-label="Member profile photo"></div>

  <table class="abs details">
    <tr><td>Name:</td><td class="name">MARLA</td></tr>
    <tr><td>Nick Name:</td><td>Marlie</td></tr>
    <tr><td>Rating</td><td class="stars">★★★★<i>★</i></td></tr>
    <tr><td>Age:</td><td>35</td></tr>
    <tr><td>Height:</td><td>5.7 feet</td></tr>
    <tr><td>Weight:</td><td>54</td></tr>
    <tr><td>Outfit:</td><td>Slim</td></tr>
    <tr><td>Hair Colour:</td><td>Blond</td></tr>
    <tr><td>Eye Colour:</td><td>Brown</td></tr>
    <tr><td>Race:</td><td>White</td></tr>
    <tr><td>Religion:</td><td>Christian</td></tr>
    <tr><td>Date Joined:</td><td>24 June, 2012</td></tr>
    <tr><td>Horoscope:</td><td>Aries</td></tr>
    <tr><td>Location:</td><td>Oregon, U.S.A.</td></tr>
    <tr><td>Interested In:</td><td>Men</td></tr>
    <tr><td>Marital Status:</td><td>Married</td></tr>
  </table>

  <div class="abs intro">
    <strong>Lorem ipsum dolor sit amet, consectetuer adipiscing elit. Praesent eredict vestibulum molestie lacus. Aenean nonum hendrerit</strong>
    Nascetur ridiculus mus. Nulla dui. Fusce feugiat malesuada odio. Morbi nunc odio, gravida at, cursus nec, luctus a, lorem. Maecenas tristique orci sem. Duis ultricies pharetra magna. Donec accumsan malesuada orci. Donec sit amet eros. Lorem ipsum dolor sit amet, consectetuer adipiscing elit.
  </div>

  <div class="abs action-btn" style="left:508px;top:160px;width:113px"><span class="ico" style="background:#a24bd6"></span>Leave a Message</div>
  <div class="abs action-btn" style="left:627px;top:160px;width:113px;gap:30px"><span class="ico" style="background:#e8592c;border-radius:2px"></span>Get a Gift</div>
  <div class="abs action-btn" style="left:508px;top:189px;width:113px"><span class="ico" style="background:#e04e2a"></span>Add to Favourite</div>
  <div class="abs action-btn" style="left:627px;top:189px;width:113px"><span class="ico" style="background:#c9262a"></span>Block a Friend</div>
  <div class="abs action-btn" style="left:508px;top:218px;width:113px;gap:6px"><span class="ico" style="background:#2f7fb0"></span>Chat with a Friend</div>

  <h2 class="abs h-section" style="left:508px;top:267px"><b>MARLA´S</b> friends</h2>
  <div class="abs friend" style="top:299px">
    <div class="face" role="img" aria-label="Friend photo"></div>
    <div class="info">Owen Castell<b>43 years</b>Nascetur ridiculus mus. Nulla dui. Fusce feugiat malesuada odio.</div>
  </div>
  <div class="abs friend" style="top:376px">
    <div class="face" role="img" aria-label="Friend photo" style="background:linear-gradient(160deg,#d9c2ad,#6d5545)"></div>
    <div class="info">Rafe Donnelly<b>38 years</b>Nascetur ridiculus mus. Nulla dui. Fusce feugiat malesuada odio.</div>
  </div>
  <a class="abs pill" style="left:509px;top:470px;width:86px">SEE ALL<span class="chev"></span></a>

  <h2 class="abs h-section" style="left:104px;top:591px"><b>MY</b> photos</h2>
  <div class="abs thumb" style="left:101px;top:635px;background:linear-gradient(135deg,#2b2c33,#c9a58c)" role="img" aria-label="Member photo"></div>
  <div class="abs thumb" style="left:221px;top:635px;background:linear-gradient(135deg,#5a4a43,#d0635a)" role="img" aria-label="Member photo"></div>
  <div class="abs thumb" style="left:341px;top:635px;background:linear-gradient(135deg,#8a6a22,#3b2f22)" role="img" aria-label="Member photo"></div>
  <div class="abs thumb" style="left:101px;top:770px;background:linear-gradient(135deg,#d8702f,#c8a48a)" role="img" aria-label="Member photo"></div>
  <div class="abs thumb" style="left:221px;top:770px;background:linear-gradient(135deg,#6b4a3a,#c47d6a)" role="img" aria-label="Member photo"></div>
  <div class="abs thumb" style="left:341px;top:770px;background:linear-gradient(135deg,#5d2a22,#b85a44)" role="img" aria-label="Member photo"></div>

  <h2 class="abs h-section" style="left:509px;top:591px"><b>ADDITIONAL</b> info</h2>
  <div class="abs add-info">
    <strong>Lorem ipsum dolor sit amet, consectetuer adipiscing elit. Praesent eredict vestibulum molestie lacus. Aenean nonum hendrerit</strong>
    <p>Nascetur ridiculus mus. Nulla dui. Fusce feugiat malesuada odio. Morbi nunc odio, gravida at, cursus nec, luctus a, lorem. Maecenas tristique orci sem. Duis ultricies pharetra magna. Donec accumsan malesuada orci. Donec sit amet eros. Lorem ipsum dolor sit amet, consectetuer adipiscing elit.</p>
    <p>Nascetur ridiculus mus. Nulla dui. Fusce feugiat malesuada odio. Morbi nunc odio, gravida at, cursus nec, luctus a, lorem. Maecenas tristique orci sem. Duis ultricies pharetra magna. Donec accumsan malesuada orci. Donec sit amet eros. Lorem ipsum dolor sit amet, consectetuer adipiscing elit.</p>
  </div>
  <a class="abs pill" style="left:508px;top:855px;width:119px">EDIT PROFILE<span class="chev"></span></a>

  <div class="abs notice-line"></div>
  <div class="abs notice-band"></div>
  <div class="abs notice-tab">THIS WEBSITE IS NOT FOR SINGLES</div>
  <p class="abs notice-text">“We are not responsible for any sexually transmitted diseases" and " We are not responsible for any marriage break-ups or any problems in consequence after the encounters." "It is the responsibility of the subscriber(member) to have enough information about the person before the encounter."</p>

  <footer>
    <div class="abs footer"></div>
    <div class="abs f-col" style="left:91px"><h3>About Us</h3><a href="#">Company Info</a><a href="#">Services</a><a href="#">Dating</a></div>
    <div class="abs f-col" style="left:260px"><h3>Advice</h3><a href="#">FAQs</a><a href="#">Account</a><a href="#">Contacts</a></div>
    <div class="abs f-col" style="left:418px"><h3>Join In</h3><a href="#">Start Up</a><a href="#">Forums</a><a href="#">Promotions</a></div>
    <div class="abs social"><span></span><span></span><span></span><span></span><span></span></div>
    <div class="abs f-brand">VelvetHarbor</div>
    <div class="abs copyright">Copyright © 2012.&nbsp; All Rights Reserved.</div>
  </footer>
</div>
</body>
</html>
```